'Private English tutoring'

I need a flyer design to advertise private English tutoring. I am offering lessons to ethnic minority groups in my local area in south Belfast. The biggest ethnic minorities groups are Chinese, Polish and Indian and African. I can teach at any level, from beginner English to advanced. The tutoring will be either one on one or small groups of four students. I can teach adults and children but my preference would be to teach adults.

The flyer would need to be easily understood by people who have English as a second language.

I am also offering proof reading and editing services to students at local universities and colleges.

Target Market(s)

Adults of ethnic minorities who may not speak or read much English

Industry/Entity Type

Tutoring

Font styles to use
Serif

Requirements
Must have
• It needs to communicate that I am an accredited TEFL (Teaching English as a Foreign language) tutor with 2 years experience and that I tutor Beginners - Advanced students. It would also need to say that I offer proof reading and editing services. It would also need to communicate the cost of lessons are £15, but there are group rates for groups of 2-4 students. It would need to include my contact details which are as follows: contact Mona Hargrove BTh at 07812609354 or email monahargroveenglish@quillpost.com
Nice to have
• In terms of design I would like it to be warm and inviting and something which would convey an atmosphere of learning for non English speakers. Other than that I don't have any preferences.
Should not have
• Nothing which is going to be offensive to ethnic minorities.
• No pictures of people

```html
<!DOCTYPE html>
<html lang="en">
<head>
<meta charset="utf-8">
<title>English Tutor Flyer</title>
<link rel="stylesheet" href="https://fonts.googleapis.com/css2?family=Alfa+Slab+One&family=Montserrat:wght@600;800&display=swap">
<style>
  :root {
    --gold: #c39a46;
    --gold-dark: #9c7731;
    --green: #2f6a3b;
    --green-dark: #1f4a28;
    --cream: #fbf4c9;
    --stripe: #f5e8a6;
    --white: #ffffff;
  }
  * { box-sizing: border-box; margin: 0; padding: 0; }
  html, body { width: 851px; height: 1200px; overflow: hidden; background: var(--cream); }
  .flyer {
    position: relative;
    width: 851px;
    height: 1200px;
    background: repeating-linear-gradient(90deg, var(--cream) 0 22px, var(--stripe) 22px 44px);
    font-family: "Montserrat", Arial, sans-serif;
  }
  .frame {
    position: absolute;
    inset: 22px;
    border: 12px solid var(--gold);
  }
  .frame::after {
    content: "";
    position: absolute;
    inset: 8px;
    border: 2px solid var(--gold);
  }
  .headline {
    position: absolute;
    top: 78px;
    left: 0;
    width: 100%;
    text-align: center;
    font-family: "Alfa Slab One", Georgia, serif;
    font-size: 132px;
    letter-spacing: 6px;
    color: var(--gold);
    text-shadow: 4px 4px 0 var(--white), 6px 6px 0 var(--gold-dark);
    line-height: 1;
  }
  .tiles {
    position: absolute;
    top: 252px;
    left: 0;
    width: 100%;
    display: flex;
    justify-content: center;
    gap: 14px;
  }
  .tile {
    width: 112px;
    height: 122px;
    background: var(--green);
    border: 4px solid var(--white);
    border-radius: 10px;
    box-shadow: 4px 4px 0 var(--green-dark);
    color: var(--white);
    font-family: "Alfa Slab One", Georgia, serif;
    font-size: 88px;
    line-height: 114px;
    text-align: center;
  }
  .banner { position: absolute; top: 420px; left: 0; width: 851px; height: 250px; }
  .banner-text {
    position: absolute;
    top: 468px;
    left: 130px;
    width: 591px;
    text-align: center;
    color: var(--white);
    font-weight: 800;
    font-size: 27px;
    line-height: 1.32;
    text-transform: uppercase;
  }
  .services {
    position: absolute;
    top: 728px;
    left: 108px;
    width: 640px;
    list-style: none;
  }
  .services li {
    display: flex;
    align-items: flex-start;
    gap: 14px;
    margin-bottom: 24px;
    color: var(--green-dark);
    font-weight: 600;
    font-size: 19px;
    line-height: 1.25;
    text-transform: uppercase;
  }
  .services svg { flex: none; width: 20px; height: 20px; margin-top: 1px; }
  .contact-ribbon { position: absolute; top: 975px; left: 0; width: 851px; height: 160px; }
  .contact-text {
    position: absolute;
    top: 1008px;
    left: 150px;
    width: 551px;
    text-align: center;
    color: var(--white);
    font-weight: 800;
    font-size: 18px;
    line-height: 1.5;
    text-transform: uppercase;
  }
</style>
</head>
<body>
<main class="flyer">
  <div class="frame"></div>

  <h1 class="headline">ENGLISH</h1>

  <div class="tiles" aria-label="Tutor">
    <span class="tile">T</span>
    <span class="tile">U</span>
    <span class="tile">T</span>
    <span class="tile">O</span>
    <span class="tile">R</span>
  </div>

  <svg class="banner" viewBox="0 0 851 250" aria-hidden="true">
    <polygon points="95,40 130,20 130,200 95,180" fill="var(--green-dark)"/>
    <polygon points="756,70 721,50 721,230 756,210" fill="var(--green-dark)"/>
    <rect x="130" y="20" width="591" height="200" fill="var(--green)"/>
  </svg>
  <p class="banner-text">Learn English with a TEFL qualified tutor with 2 years experience in the field of teaching</p>

  <ul class="services">
    <li><svg viewBox="0 0 20 20"><polygon points="10,1 12.6,7 19,7.4 14,11.6 15.6,18 10,14.5 4.4,18 6,11.6 1,7.4 7.4,7" fill="var(--green)"/></svg>Classes for both beginners and advanced level students.</li>
    <li><svg viewBox="0 0 20 20"><polygon points="10,1 12.6,7 19,7.4 14,11.6 15.6,18 10,14.5 4.4,18 6,11.6 1,7.4 7.4,7" fill="var(--green)"/></svg>Both individual and group lessons available at request.</li>
    <li><svg viewBox="0 0 20 20"><polygon points="10,1 12.6,7 19,7.4 14,11.6 15.6,18 10,14.5 4.4,18 6,11.6 1,7.4 7.4,7" fill="var(--green)"/></svg>£15 per lesson (for group class rates please contact us)</li>
    <li><svg viewBox="0 0 20 20"><polygon points="10,1 12.6,7 19,7.4 14,11.6 15.6,18 10,14.5 4.4,18 6,11.6 1,7.4 7.4,7" fill="var(--green)"/></svg>Proof reading and editing services available.</li>
  </ul>

  <svg class="contact-ribbon" viewBox="0 0 851 160" aria-hidden="true">
    <polygon points="95,40 205,40 205,145 95,145 130,92" fill="var(--green)"/>
    <polygon points="756,40 646,40 646,145 756,145 721,92" fill="var(--green)"/>
    <polygon points="150,120 205,145 205,120" fill="var(--green-dark)"/>
    <polygon points="701,120 646,145 646,120" fill="var(--green-dark)"/>
    <rect x="150" y="15" width="551" height="105" fill="var(--green)"/>
  </svg>
  <p class="contact-text">Contact Mona Hargrove BTh at 07812609354<br>or email monahargroveenglish@quillpost.com</p>
</main>
</body>
</html>
```